Business cards and stationary
IT Consultancy
Professional
Dermot Ashby
Managing Director
27 Larch Chambers
62 Pellbrook Gardens
Ashcombe
Wexmoor
TW3 5RJ
dermot.ashby@brevix.com
www.brevix.com
Would like to incorporate both types of logos (white on black and black on white)
Also, like an A4 folder design to house brochures.

```html
<!DOCTYPE html>
<html lang="en">
<head>
<meta charset="utf-8">
<title>Brevix business card</title>
<link rel="stylesheet" href="https://fonts.googleapis.com/css2?family=Source+Sans+3:wght@400;600;700&display=swap">
<style>
  :root {
    --page-bg: #e9eaec;
    --card-white: #ffffff;
    --ink: #2b2b2b;
    --accent-red: #d3202f;
    --brand-blue: #1b4f8f;
    --navy-light: #2a5ea8;
    --navy-dark: #0d2350;
    --rule-grey: #c9cbce;
  }
  html, body {
    margin: 0;
    width: 1200px;
    height: 930px;
    overflow: hidden;
    background: var(--page-bg);
    font-family: "Source Sans 3", Arial, sans-serif;
  }
  .card {
    position: absolute;
    left: 290px;
    width: 597px;
    height: 348px;
    box-sizing: border-box;
  }
  .card-front { top: 106px; background: var(--card-white); }
  .card-back {
    top: 474px;
    background: radial-gradient(ellipse at 45% 45%, var(--navy-light) 0%, #17407f 40%, var(--navy-dark) 100%);
  }
  .brand {
    position: absolute;
    display: flex;
    align-items: center;
    gap: 14px;
  }
  .brand-mark { width: 34px; height: 34px; border-radius: 50%; }
  .brand-name { font-weight: 700; font-size: 44px; letter-spacing: 1px; line-height: 1; }
  .card-front .brand { left: 63px; top: 136px; }
  .card-front .brand-mark { background: var(--brand-blue); }
  .card-front .brand-name { color: var(--brand-blue); }
  .card-back .brand { left: 90px; top: 150px; }
  .card-back .brand-mark { background: #ffffff; }
  .card-back .brand-name { color: #ffffff; }
  .contact {
    position: absolute;
    left: 360px;
    top: 28px;
    color: var(--ink);
    font-size: 16px;
    line-height: 20px;
  }
  .contact-name { font-weight: 700; font-size: 25px; line-height: 28px; margin: 0; }
  .contact-role { color: var(--accent-red); font-size: 17px; margin: 0 0 22px; }
  .address, .lines { margin: 0 0 14px; }
  .label { color: var(--accent-red); font-weight: 700; }
  .bands { position: absolute; left: 0; right: 0; top: 326px; height: 12px; }
  .band-rule { position: absolute; left: 0; right: 0; top: 5px; height: 2px; background: var(--rule-grey); }
  .band-red { position: absolute; left: 140px; width: 210px; height: 12px; background: linear-gradient(90deg, rgba(211,32,47,0), var(--accent-red) 40%); }
  .band-blue { position: absolute; left: 364px; right: 0; height: 12px; background: var(--brand-blue); }
  .web {
    position: absolute;
    left: 335px;
    top: 170px;
    color: #ffffff;
    font-size: 20px;
    letter-spacing: 0.5px;
  }
</style>
</head>
<body>
  <section class="card card-front">
    <div class="brand"><span class="brand-mark"></span><span class="brand-name">Brevix</span></div>
    <div class="contact">
      <p class="contact-name">Dermot Ashby</p>
      <p class="contact-role">Managing Director</p>
      <p class="address">27 Larch Chambers<br>62 Pellbrook Gardens<br>Ashcombe, Wexmoor<br>TW3 5RJ</p>
      <p class="lines"><span class="label">P</span> 01632 960 418<br><span class="label">C</span> 07700 900 572<br><span class="label">E</span> dermot.ashby@brevix.com</p>
    </div>
    <div class="bands">
      <div class="band-rule"></div>
      <div class="band-red"></div>
      <div class="band-blue"></div>
    </div>
  </section>
  <section class="card card-back">
    <div class="brand"><span class="brand-mark"></span><span class="brand-name">Brevix</span></div>
    <div class="web">www.brevix.com</div>
  </section>
</body>
</html>
```